Resort Room Letter to go in Welcome Basket

It needs the Resort Logo and a snazzier font. Probably some kind of background. It will be in full color. Dimensions 5.5in x 8in. This is the in room letter that goes with the welcome basket.

Text:

Welcome to The Resort! We have prepared this convenient Starter Pack to enhance your stay in our Luxury Condominiums. To further enhance your stay housekeeping will provide daily limited service which includes fresh towels and trash removal. Additional housekeeping services can be scheduled with the front desk for a nominal fee. Please leave the basket so that we can prepare a Starter Pack for the next guest. When you are ready to checkout simply dial **47.

Helpful Hints:

Turn the lever in the freezer to start making ice
The Waterpark can be accessed from the 1st Floor
The Indoor Waterpark is open from 9AM to 11PM
Vending with Snacks & Drinks are available on Floors 1, 2, 4, & 5
The closest grocery store is Brindlemart
You can also conveniently order groceries via Pantrygo from Halvey, Grain Town, & Tamrel
Additional convenience items are available for purchase at the Front Desk
Use our Express Checkout by Dialing **47

Thank you so much for choosing the Resort for your Smoky Mountain Vacation!

The Resort Management Team

```html
<!DOCTYPE html>
<html lang="en">
<head>
<meta charset="utf-8">
<title>Welcome to The Resort</title>
<link rel="stylesheet" href="https://fonts.googleapis.com/css2?family=Pinyon+Script&family=Didact+Gothic&family=Oswald:wght@400&family=Montserrat:wght@500;700&display=swap">
<style>
  :root {
    --paper: #fdfcf8;
    --paper-shade: #f3efe6;
    --brown: #6a4a2c;
    --ink: #4a4038;
    --gold: #c49a55;
    --gold-soft: #e2cfa6;
  }
  * { margin: 0; padding: 0; box-sizing: border-box; }
  html, body { width: 825px; height: 1200px; overflow: hidden; background: var(--paper); }
  .letter {
    position: relative; width: 825px; height: 1200px; overflow: hidden;
    background: radial-gradient(ellipse at center, var(--paper) 55%, var(--paper-shade) 100%);
    color: var(--ink);
    font-family: "Didact Gothic", "Century Gothic", sans-serif;
  }
  .corner-ornament { position: absolute; }
  .corner-ornament.top-left { left: 0; top: 0; width: 145px; height: 125px; background: linear-gradient(135deg, var(--gold-soft), rgba(226,207,166,0)); }
  .corner-ornament.top-right { right: 0; top: 0; width: 145px; height: 125px; background: linear-gradient(225deg, var(--gold-soft), rgba(226,207,166,0)); }
  .corner-ornament.bottom-left { left: 0; bottom: 0; width: 115px; height: 135px; background: linear-gradient(45deg, var(--gold-soft), rgba(226,207,166,0)); }
  .corner-ornament.bottom-right { right: 0; bottom: 0; width: 115px; height: 135px; background: linear-gradient(315deg, var(--gold-soft), rgba(226,207,166,0)); }

  .brand {
    position: absolute; top: 22px; left: 0; width: 825px; text-align: center;
    font-family: "Montserrat", sans-serif; font-weight: 700; color: var(--brown);
  }
  .brand-mark { display: inline-block; width: 14px; height: 14px; background: var(--gold); margin-bottom: 10px; }
  .brand-name { font-size: 30px; letter-spacing: 3px; line-height: 1.1; }
  .brand-place { font-size: 14px; letter-spacing: 2px; margin-top: 4px; }

  .headline {
    position: absolute; top: 238px; left: 0; width: 825px; text-align: center;
    font-family: "Pinyon Script", cursive; font-size: 56px; line-height: 70px; color: var(--brown); font-weight: 400;
  }
  .intro {
    position: absolute; top: 318px; left: 83px; width: 667px;
    font-size: 21px; line-height: 31px; text-align: justify;
  }
  .drop-cap {
    float: left; width: 78px; height: 62px; margin: 0 10px 0 -55px;
    font-family: "Pinyon Script", cursive; font-size: 84px; line-height: 70px;
    color: var(--brown); overflow: visible;
  }
  .divider { position: absolute; height: 14px; background: linear-gradient(90deg, rgba(196,154,85,0), var(--gold), rgba(196,154,85,0)); }
  .divider.upper { top: 540px; left: 292px; width: 260px; }
  .divider.lower { top: 852px; left: 308px; width: 224px; }

  .hints-title {
    position: absolute; top: 566px; left: 0; width: 825px; text-align: center;
    font-family: "Oswald", sans-serif; font-weight: 400; font-size: 36px; line-height: 48px; letter-spacing: 1px; color: var(--brown);
  }
  .hints-title::before, .hints-title::after {
    content: ""; display: inline-block; width: 100px; height: 2px; background: var(--gold);
    vertical-align: middle; margin: 0 22px;
  }
  .hints { position: absolute; top: 620px; left: 44px; width: 706px; list-style: none; font-size: 20px; line-height: 23px; text-align: justify; }
  .hints li { position: relative; padding-left: 20px; }
  .hints li::before {
    content: ""; position: absolute; left: 0; top: 6px; width: 11px; height: 11px; background: var(--gold);
    clip-path: polygon(50% 0, 62% 38%, 100% 50%, 62% 62%, 50% 100%, 38% 62%, 0 50%, 38% 38%);
  }
  .hints li.continued::before { display: none; }
  .hints strong { font-family: "Montserrat", sans-serif; font-weight: 700; font-size: 18px; color: var(--ink); }

  .thanks {
    position: absolute; top: 960px; left: 0; width: 825px; text-align: center;
    font-family: "Pinyon Script", cursive; font-size: 30px; line-height: 34px; color: var(--brown);
  }
  .signoff {
    position: absolute; top: 1056px; left: 0; width: 825px; text-align: center;
    font-family: "Montserrat", sans-serif; font-weight: 500; font-size: 17px; color: var(--ink);
  }
</style>
</head>
<body>
<main class="letter">
  <div class="corner-ornament top-left" role="img" aria-label="Gold flourish corner ornament"></div>
  <div class="corner-ornament top-right" role="img" aria-label="Gold flourish corner ornament"></div>
  <div class="corner-ornament bottom-left" role="img" aria-label="Gold flourish corner ornament"></div>
  <div class="corner-ornament bottom-right" role="img" aria-label="Gold flourish corner ornament"></div>

  <header class="brand">
    <span class="brand-mark"></span>
    <div class="brand-name">THE RESORT</div>
    <div class="brand-place">AT HOLLIN CROSSING</div>
  </header>

  <h1 class="headline">Welcome to The Resort!</h1>

  <p class="intro"><span class="drop-cap">W</span>e have prepared this convenient Starter Pack to enhance your stay in our Luxury Condominiums. To further enhance your stay housekeeping will provide daily limited service which includes fresh towels and trash removal. Additional housekeeping services can be scheduled with the front desk for a nominal fee. Please leave the basket so that we can prepare a Starter Pack for the next guest. When you are ready to checkout simply dial **47.</p>

  <div class="divider upper" role="img" aria-label="Gold scroll divider ornament"></div>

  <h2 class="hints-title">HELPFUL HINTS</h2>

  <ul class="hints">
    <li>Turn the lever in the freezer to start <strong>making ice</strong>.</li>
    <li><strong>The Waterpark</strong> can be accessed from the 1st Floor.</li>
    <li>The Indoor Waterpark is open from <strong>9AM to 11PM</strong>.</li>
    <li>Vending with <strong>Snacks &amp; Drinks</strong> are available on Floors 1, 2, 4, &amp; 5.</li>
    <li>The closest grocery store is <strong>Brindlemart</strong>.</li>
    <li>You can also conveniently <strong>order groceries</strong> via Pantrygo from Halvey, Grain Town, &amp; Tamrel.</li>
    <li><strong>Additional</strong> convenience items are available for purchase at the Front&nbsp;Desk&nbsp;.</li>
    <li class="continued">Use our Express Checkout by <strong>Dialing **47</strong>.</li>
  </ul>

  <div class="divider lower" role="img" aria-label="Gold scroll divider ornament"></div>

  <p class="thanks">Thank you so much for choosing<br>the Resort for your Smoky Mountain Vacation!</p>
  <p class="signoff">The Resort Management Team.</p>
</main>
</body>
</html>
```